Products & Services Postcard For our Vacuum Repair Store & Carpet Cleaning Company

SEE ATTACHED DOCUMENTS FOR FRONT AND BACK OF CARD.
Also, Brand logos are available in my attachments

We are a Retail Vacuum Repair shop and we also have Three carpet cleaning trucks that operate out of our location. In addition to servicing Vacuum Cleaners we also offer in home cleaning services that include: Carpet cleaning, upholstery cleaning, tile & Grout Cleaning, general cleaning services, move out clean ups, one time cleanings, post construction cleanup and strip & wax floorsWe Need to design a KRTB(pvlo quiet lane parcel) postcard that shows and tells everything we do. Postcard should include all our services, have before and after pictures, list benefits of doing business with us and should have coupons attached to create urgency to call usWe:Fully Insured, commercial & Residential, free estimatesWe are the only Vacuum Store in area that is a Certified SVAPN Cleaner.Also, the only SVAPN Certified cleaner that services Vacuum Cleaners.We have a great reputation as a 5 Star Vacuum Service Station and Also a 5 Star Cleaning Company. We are a one stop shop for ALL your cleaning needs.Our goal is to educate customers and provide options.Goal of the card is to get customers to call or stop in for advice on both their vacuum cleaner and cleaning their homes. Goal is to get phone to ring or get people through the door.

Target Market(s)

Homeowners, People interested in clean

Colors

Designer to choose colors to be used in the design.

Requirements
Must have
• Before & After pics
• Coupons
• List of services
• Call to Action
• Address
• Phone #
Nice to have
• One side of postcard could be about our Vacuum Cleaner repair shop.
• The other side could be about our cleaning business

```html
<!DOCTYPE html>
<html lang="en">
<head>
<meta charset="utf-8">
<title>Crestline Vacuums Postcard</title>
<link rel="stylesheet" href="https://fonts.googleapis.com/css2?family=Bebas+Neue&family=Lato:ital,wght@0,400;0,700;0,900;1,700&family=Montserrat:wght@700;800&family=Oswald:wght@400;500;600&display=swap">
<style>
:root{
  --stage:#4b4b4b;
  --teal:#147a78;
  --teal-dark:#0d5c5e;
  --cyan:#27b7d1;
  --yellow:#f1dc1e;
  --green:#2fb24b;
  --orange:#e6501c;
  --ink:#1d3a3c;
  --paper:#ffffff;
  --light:#e9ecec;
}
*{box-sizing:border-box;margin:0;padding:0}
html,body{width:900px;height:1200px;overflow:hidden}
body{background:var(--stage);position:relative;font-family:'Lato',sans-serif}
.card{position:absolute;left:93px;width:724px;height:510px;background:var(--paper);overflow:hidden}
.card--front{top:60px;background:var(--light)}
.card--back{top:625px}
.abs{position:absolute}
svg.layer{position:absolute;left:0;top:0}

/* front */
.header-band{left:0;top:0;width:724px;height:78px;background:linear-gradient(90deg,#7d9591,#a9b8b5)}
.brand{left:18px;top:46px;font:800 15px 'Montserrat',sans-serif;color:var(--ink);line-height:1;display:flex;align-items:center;gap:6px}
.brand .dot{width:12px;height:12px;border-radius:50%;background:var(--ink)}
.tagline{left:138px;top:28px;font:italic 700 13px 'Lato',sans-serif;color:#fff}
.header-phone{left:257px;top:57px;font:400 13px 'Lato',sans-serif;color:#2b3b3c}
.hero-photo{left:380px;top:0;width:344px;height:340px;background:linear-gradient(120deg,#e9e2d5 0%,#d8c6a6 45%,#8a6a48 80%,#5c4632 100%)}
.estimate-ribbon{left:595px;top:0;width:122px;height:122px}
.estimate-text{left:597px;top:16px;width:118px;text-align:center;color:#1d2a2a;font:700 12px 'Lato',sans-serif;line-height:1.05}
.estimate-text .free{display:block;color:var(--orange);font:800 24px 'Montserrat',sans-serif;line-height:1}
.estimate-text .all{display:block;font:900 14px 'Lato',sans-serif}
.estimate-text .small{display:block;font-size:9px}
.headline-bar{left:0;top:103px;width:420px;height:50px;background:var(--yellow)}
.headline{left:22px;top:109px;font:800 18px 'Montserrat',sans-serif;color:var(--ink);white-space:nowrap}
.subhead{left:78px;top:135px;font:700 11px 'Lato',sans-serif;letter-spacing:4px;color:var(--ink)}
.services{left:22px;top:172px;list-style:none}
.services li{font:700 11.5px 'Lato',sans-serif;color:#223;line-height:14.3px;display:flex;align-items:center;gap:5px}
.tick{width:10px;height:10px;flex:none}
.report-badge{left:233px;top:190px;width:124px;height:124px;border-radius:50%;background:radial-gradient(circle at 40% 35%,#5fd36d,var(--green) 60%,#1f8c37);border:4px solid #fff;box-shadow:0 0 0 2px #cfd7d6;text-align:center;color:#fff;overflow:hidden}
.report-badge .visit{display:block;margin-top:16px;font:500 9px 'Oswald',sans-serif;line-height:1.15;text-transform:uppercase;white-space:nowrap}
.report-badge .big{display:block;font:400 34px 'Bebas Neue',sans-serif;line-height:.95}
.report-badge .small{display:block;font:400 7px 'Oswald',sans-serif;line-height:1.15;text-transform:uppercase;padding:0 16px}
.proof{width:124px;height:124px;border-radius:50%;border:4px solid #fff;box-shadow:0 2px 6px rgba(0,0,0,.3)}
.proof--before{left:412px;top:258px;background:radial-gradient(circle,#a39080,#7c6a5b)}
.proof--after{left:556px;top:256px;background:linear-gradient(135deg,#c9b8a6,#9d8a77)}
.proof-label{font:700 22px 'Lato',sans-serif;color:#fff;text-shadow:0 1px 3px rgba(0,0,0,.5)}
.proof-label--before{left:445px;top:278px}
.proof-label--after{left:598px;top:260px}
.trust{left:26px;top:340px;font:600 12.5px 'Oswald',sans-serif;color:#fff;letter-spacing:.5px;line-height:26px}
.trust .hl{color:var(--yellow)}
.coupon-row{left:0;top:400px;width:724px;height:90px;background:#eceeee}
.footer-strip{left:0;top:488px;width:724px;height:22px;background:var(--teal-dark)}
.coupon{top:404px;width:106px;height:82px;border-radius:5px;background:#fff;border:1px dashed #9fb3b3;overflow:hidden}
.coupon__deal{height:56px;background:var(--cyan);color:#fff;text-align:center;position:relative}
.coupon__note{display:block;font:400 6px 'Oswald',sans-serif;text-transform:uppercase;line-height:1.1;padding:4px 6px 0}
.coupon__price{font:400 30px 'Bebas Neue',sans-serif;color:var(--yellow);line-height:1}
.coupon__pre{display:inline-block;font:400 11px 'Bebas Neue',sans-serif;color:var(--yellow);transform:rotate(-90deg);vertical-align:8px;margin-right:-4px}
.coupon__fine{display:block;font:400 5.5px 'Oswald',sans-serif;text-transform:uppercase;margin-top:-2px}
.coupon__label{text-align:center;font:400 19px 'Bebas Neue',sans-serif;color:var(--teal);line-height:24px;letter-spacing:.5px}

/* back */
.frustrated{left:26px;top:28px;color:#fff;font:800 26px 'Montserrat',sans-serif;line-height:1}
.frustrated small{display:block;font-size:17.5px;margin-top:4px}
.tuneup-bar{left:0;top:90px;width:292px;height:48px}
.tuneup-label{left:28px;top:104px;font:400 22px 'Bebas Neue',sans-serif;color:var(--orange);letter-spacing:.5px}
.tuneup-price{left:196px;top:96px;font:400 38px 'Bebas Neue',sans-serif;color:#fff;line-height:1}
.tuneup-price .pre{display:inline-block;font-size:15px;transform:rotate(-90deg);vertical-align:10px;margin-right:-6px;color:var(--yellow)}
.tuneup-fine{left:30px;top:144px;font:400 6.5px 'Lato',sans-serif;color:#fff;line-height:1.2}
.shop-line{left:26px;top:183px;font:700 12px 'Montserrat',sans-serif;color:var(--yellow);white-space:nowrap;z-index:2}
.offer-pill{left:0;top:216px;width:104px;height:22px;border-radius:0 12px 12px 0;background:linear-gradient(#f4f4f4,#cfd3d3);font:700 13px 'Lato',sans-serif;color:#2a3a3a;padding:3px 0 0 28px}
.offers{left:26px;top:256px;list-style:none}
.offers li{font:700 11.5px 'Lato',sans-serif;color:#fff;line-height:18.6px;display:flex;align-items:center;gap:8px}
.curbside{left:26px;top:362px;font:700 10.5px 'Lato',sans-serif;color:#fff;line-height:15px;width:270px}
.work-photo{border-radius:50%;border:4px solid #fff;box-shadow:0 2px 6px rgba(0,0,0,.35)}
.work-photo--carpet{left:242px;top:212px;width:126px;height:126px;background:linear-gradient(135deg,#a7a69c,#d9d6ca 50%,#8d8b80)}
.work-photo--tile{left:304px;top:312px;width:76px;height:76px;background:linear-gradient(135deg,#c9c1ae,#9f9683)}
.contact-band{left:0;top:415px;width:376px;height:75px;background:var(--cyan)}
.address{left:50px;top:429px;font:400 14px 'Bebas Neue',sans-serif;color:#fff;line-height:16px;letter-spacing:.5px}
.address small{display:block;font:400 8px 'Oswald',sans-serif}
.back-phone{left:254px;top:436px;font:400 22px 'Bebas Neue',sans-serif;color:#fff;letter-spacing:.5px}
.makes-banner{left:426px;top:0;width:268px;height:280px}
.makes-title{left:426px;top:40px;width:268px;text-align:center;font:600 12px 'Oswald',sans-serif;color:#222}
.makes{left:440px;top:78px;width:246px;display:flex;flex-wrap:wrap;column-gap:10px;row-gap:13px;align-items:center}
.make{font:800 11px 'Montserrat',sans-serif;line-height:1}
.mailing-box{left:422px;top:355px;width:272px;height:120px;border:1px solid #333;border-radius:14px}
.mailing-line{left:450px;width:212px;height:1px;background:#333}
</style>
</head>
<body>

<!-- FRONT -->
<section class="card card--front">
  <div class="abs header-band"></div>
  <div class="abs brand"><span class="dot"></span>CRESTLINE VACUUMS</div>
  <p class="abs tagline">“Nobody Does It Better &amp; Gives You More”</p>
  <p class="abs header-phone">Call 555-014-2290</p>

  <div class="abs hero-photo" role="img" aria-label="Woman vacuuming a sunlit living room floor"></div>

  <svg class="layer" width="724" height="410" viewBox="0 0 724 410" aria-hidden="true">
    <path d="M402,0 C372,110 372,230 436,340" fill="none" stroke="var(--cyan)" stroke-width="16"/>
    <path d="M388,0 C358,120 360,240 422,345" fill="none" stroke="var(--yellow)" stroke-width="5"/>
    <path d="M0,318 C180,286 320,300 460,335 C560,360 650,345 724,322 L724,410 L0,410 Z" fill="var(--teal)"/>
    <path d="M0,312 C180,280 320,294 460,329 C560,354 650,339 724,316" fill="none" stroke="var(--yellow)" stroke-width="4"/>
    <path d="M0,340 C200,318 340,330 724,350 L724,410 L0,410 Z" fill="var(--teal-dark)" opacity=".5"/>
  </svg>

  <svg class="abs estimate-ribbon" viewBox="0 0 122 122" aria-hidden="true">
    <path d="M2,0 H120 V108 L61,122 L2,108 Z" fill="var(--yellow)"/>
  </svg>
  <p class="abs estimate-text">Call us for a<span class="free">FREE</span>Estimates on<span class="all">ALL YOUR</span><span class="small">Cleaning Needs!</span></p>

  <div class="abs headline-bar"></div>
  <h1 class="abs headline">CARPETS &amp; FLOORING NEED CLEANING?</h1>
  <p class="abs subhead">Furniture Need Cleaning?</p>

  <ul class="abs services">
    <li><svg class="tick" viewBox="0 0 10 10"><circle cx="5" cy="5" r="5" fill="var(--cyan)"/><path d="M2.5,5 L4.3,6.8 L7.6,3.4" stroke="#fff" stroke-width="1.4" fill="none"/></svg>Commercial</li>
    <li><svg class="tick" viewBox="0 0 10 10"><circle cx="5" cy="5" r="5" fill="var(--cyan)"/><path d="M2.5,5 L4.3,6.8 L7.6,3.4" stroke="#fff" stroke-width="1.4" fill="none"/></svg>Residential</li>
    <li><svg class="tick" viewBox="0 0 10 10"><circle cx="5" cy="5" r="5" fill="var(--cyan)"/><path d="M2.5,5 L4.3,6.8 L7.6,3.4" stroke="#fff" stroke-width="1.4" fill="none"/></svg>General Cleaning</li>
    <li><svg class="tick" viewBox="0 0 10 10"><circle cx="5" cy="5" r="5" fill="var(--cyan)"/><path d="M2.5,5 L4.3,6.8 L7.6,3.4" stroke="#fff" stroke-width="1.4" fill="none"/></svg>Move In &amp; Move Out Cleanings</li>
    <li><svg class="tick" viewBox="0 0 10 10"><circle cx="5" cy="5" r="5" fill="var(--cyan)"/><path d="M2.5,5 L4.3,6.8 L7.6,3.4" stroke="#fff" stroke-width="1.4" fill="none"/></svg>Carpet Cleaning</li>
    <li><svg class="tick" viewBox="0 0 10 10"><circle cx="5" cy="5" r="5" fill="var(--cyan)"/><path d="M2.5,5 L4.3,6.8 L7.6,3.4" stroke="#fff" stroke-width="1.4" fill="none"/></svg>Tile &amp; Grout Cleaning</li>
    <li><svg class="tick" viewBox="0 0 10 10"><circle cx="5" cy="5" r="5" fill="var(--cyan)"/><path d="M2.5,5 L4.3,6.8 L7.6,3.4" stroke="#fff" stroke-width="1.4" fill="none"/></svg>VCT Strip &amp; Wax</li>
    <li><svg class="tick" viewBox="0 0 10 10"><circle cx="5" cy="5" r="5" fill="var(--cyan)"/><path d="M2.5,5 L4.3,6.8 L7.6,3.4" stroke="#fff" stroke-width="1.4" fill="none"/></svg>Furniture Cleaning</li>
  </ul>

  <div class="abs report-badge">
    <span class="visit">Visit<br>crestlinevacuums.com<br>and get your</span>
    <span class="big">FREE</span>
    <span class="small">Report on “How to choose a cleaning company”</span>
  </div>

  <div class="abs proof proof--before" role="img" aria-label="Worn carpet before cleaning"></div>
  <div class="abs proof proof--after" role="img" aria-label="Freshly cleaned carpet after cleaning"></div>
  <p class="abs proof-label proof-label--before">Before</p>
  <p class="abs proof-label proof-label--after">After</p>

  <p class="abs trust">FRIENDLY, PROFESSIONAL, SVAPN TRAINED TECHNICIANS<br>FINDLY <span class="hl">“CRESTLINE VACUUMS”</span> FOR REVIEWS.</p>

  <div class="abs coupon-row"></div>
  <div class="abs footer-strip"></div>

  <div class="abs coupon" style="left:52px">
    <div class="coupon__deal"><span class="coupon__note">Whole house carpet cleaning up to 700 sq ft</span><span class="coupon__pre">Only</span><span class="coupon__price">$189</span></div>
    <p class="coupon__label">Coupon 1</p>
  </div>
  <div class="abs coupon" style="left:182px">
    <div class="coupon__deal"><span class="coupon__note">Furniture cleaning</span><span class="coupon__price">$199</span><span class="coupon__fine">(Sofa, loveseat &amp; chair)</span></div>
    <p class="coupon__label">Coupon 2</p>
  </div>
  <div class="abs coupon" style="left:312px">
    <div class="coupon__deal"><span class="coupon__note">Tile &amp; grout cleaning kitchen floor</span><span class="coupon__pre">Only</span><span class="coupon__price">$119</span></div>
    <p class="coupon__label">Coupon 3</p>
  </div>
  <div class="abs coupon" style="left:442px">
    <div class="coupon__deal"><span class="coupon__note">Free cleaning kit</span><span class="coupon__pre">Value of</span><span class="coupon__price">$59</span><span class="coupon__fine">For your carpet when you add protector</span></div>
    <p class="coupon__label">Coupon 4</p>
  </div>
  <div class="abs coupon" style="left:572px">
    <div class="coupon__deal"><span class="coupon__note">Free tile &amp; grout cleaning kit</span><span class="coupon__pre">Value of</span><span class="coupon__price">$59</span><span class="coupon__fine">When you add sealer</span></div>
    <p class="coupon__label">Coupon 5</p>
  </div>
</section>

<!-- BACK -->
<section class="card card--back">
  <svg class="layer" width="724" height="510" viewBox="0 0 724 510" aria-hidden="true">
    <path d="M0,0 H372 C420,130 420,290 376,415 H0 Z" fill="var(--teal)"/>
    <path d="M385,0 C436,130 436,300 392,430" fill="none" stroke="var(--cyan)" stroke-width="14"/>
    <path d="M400,0 C452,130 452,300 408,432" fill="none" stroke="var(--yellow)" stroke-width="4"/>
    <rect x="0" y="490" width="724" height="20" fill="var(--teal-dark)"/>
  </svg>

  <h2 class="abs frustrated">ARE YOU FRUSTRATED<small>WITH YOUR VACUUM CLEANER?!</small></h2>

  <svg class="abs tuneup-bar" viewBox="0 0 292 48" aria-hidden="true">
    <path d="M0,4 H184 L172,44 H0 Z" fill="var(--yellow)"/>
    <path d="M184,0 H292 V48 H170 Z" fill="var(--orange)"/>
  </svg>
  <p class="abs tuneup-label">VACUUM TUNE UP</p>
  <p class="abs tuneup-price"><span class="pre">Only</span>$19.99</p>
  <p class="abs tuneup-fine">*Offer Expires in 30 days<br>*Limit One Vacuum Per Coupon</p>

  <div class="abs work-photo work-photo--carpet" role="img" aria-label="Carpet being cleaned with an extraction wand"></div>
  <div class="abs work-photo work-photo--tile" role="img" aria-label="Tile floor with grout being cleaned"></div>

  <p class="abs shop-line">FIVE STAR VACUUM CLEANER REPAIR SHOP</p>
  <p class="abs offer-pill">We Offer</p>

  <ul class="abs offers">
    <li><svg class="tick" viewBox="0 0 10 10"><circle cx="5" cy="5" r="5" fill="var(--yellow)"/><path d="M2.5,5 L4.3,6.8 L7.6,3.4" stroke="var(--teal)" stroke-width="1.5" fill="none"/></svg>Free Estimates</li>
    <li><svg class="tick" viewBox="0 0 10 10"><circle cx="5" cy="5" r="5" fill="var(--yellow)"/><path d="M2.5,5 L4.3,6.8 L7.6,3.4" stroke="var(--teal)" stroke-width="1.5" fill="none"/></svg>Experienced &amp; Trained Technicians</li>
    <li><svg class="tick" viewBox="0 0 10 10"><circle cx="5" cy="5" r="5" fill="var(--yellow)"/><path d="M2.5,5 L4.3,6.8 L7.6,3.4" stroke="var(--teal)" stroke-width="1.5" fill="none"/></svg>Fast, reliable service</li>
    <li><svg class="tick" viewBox="0 0 10 10"><circle cx="5" cy="5" r="5" fill="var(--yellow)"/><path d="M2.5,5 L4.3,6.8 L7.6,3.4" stroke="var(--teal)" stroke-width="1.5" fill="none"/></svg>Courtesy(loaner vacuums)</li>
    <li><svg class="tick" viewBox="0 0 10 10"><circle cx="5" cy="5" r="5" fill="var(--yellow)"/><path d="M2.5,5 L4.3,6.8 L7.6,3.4" stroke="var(--teal)" stroke-width="1.5" fill="none"/></svg>Drive Up (Curbside Service)</li>
  </ul>

  <p class="abs curbside">(PULL IN, HONK, CALL OR BLINK YOUR LIGHTS AND WE’LL CARRY THE VACUUM IN FOR YOU)</p>

  <div class="abs contact-band"></div>
  <svg class="abs" style="left:26px;top:436px" width="14" height="20" viewBox="0 0 14 20" aria-hidden="true">
    <path d="M7,0 C3,0 0,3 0,7 C0,12 7,20 7,20 C7,20 14,12 14,7 C14,3 11,0 7,0 Z" fill="#fff"/><circle cx="7" cy="7" r="2.6" fill="var(--cyan)"/>
  </svg>
  <p class="abs address">2750 MAPLE RIDGE RD<br>FAIRHAVEN, NY 10099<small>*JUST OFF RTE 9 EXIT 4</small></p>
  <svg class="abs" style="left:228px;top:438px" width="18" height="18" viewBox="0 0 24 24" aria-hidden="true">
    <path d="M6.6,10.8 C8,13.6 10.4,16 13.2,17.4 L15.4,15.2 C15.7,14.9 16.1,14.8 16.4,15 C17.5,15.4 18.7,15.6 20,15.6 C20.6,15.6 21,16 21,16.6 V20 C21,20.6 20.6,21 20,21 C10.6,21 3,13.4 3,4 C3,3.4 3.4,3 4,3 H7.5 C8.1,3 8.5,3.4 8.5,4 C8.5,5.3 8.7,6.5 9.1,7.6 C9.2,7.9 9.1,8.3 8.9,8.6 Z" fill="#fff"/>
  </svg>
  <p class="abs back-phone">555-014-2290</p>

  <svg class="abs makes-banner" viewBox="0 0 268 280" aria-hidden="true">
    <defs><linearGradient id="bannerShade" x1="0" y1="0" x2="1" y2="0"><stop offset="0" stop-color="#e4e4e4"/><stop offset=".5" stop-color="#f8f8f8"/><stop offset="1" stop-color="#e2e2e2"/></linearGradient></defs>
    <path d="M0,0 H268 V280 L134,246 L0,280 Z" fill="url(#bannerShade)"/>
  </svg>
  <p class="abs makes-title">WE SERVICE ALL MAKES &amp; MODELS INCLUDING:</p>
  <div class="abs makes">
    <span class="make" style="color:#d42027">SORELL</span>
    <span class="make" style="color:#222">velkor</span>
    <span class="make" style="color:#1e3f8f">TARN</span>
    <span class="make" style="color:#d42027">LUMORA</span>
    <span class="make" style="color:#c8102e">KESTREL</span>
    <span class="make" style="color:#c8102e">Dust Drake</span>
    <span class="make" style="color:#222">CIVICA</span>
    <span class="make" style="color:#1e3f8f">Vacu-Nest</span>
    <span class="make" style="color:#222">Plainway</span>
    <span class="make" style="color:#c8102e">Orbivac</span>
    <span class="make" style="color:#1e3f8f">HALDEN</span>
    <span class="make" style="color:#c8102e">Brisa</span>
    <span class="make" style="color:#a4001d">NORVO</span>
    <span class="make" style="color:#1e3f8f">Calloway</span>
    <span class="make" style="color:#1e3f8f">TRUECRAFT</span>
    <span class="make" style="color:#1e3f8f">PELLAN</span>
    <span class="make" style="color:#c8102e">Cleanvale</span>
    <span class="make" style="color:#444">MARLOW</span>
  </div>

  <div class="abs mailing-box"></div>
  <div class="abs mailing-line" style="top:380px"></div>
  <div class="abs mailing-line" style="top:403px"></div>
  <div class="abs mailing-line" style="top:427px"></div>
  <div class="abs mailing-line" style="top:451px"></div>
</section>

</body>
</html>
```